Creative, Modern and Conversion based Web Design

Kolvex Digital has recently launched a new logo and as part of our companies rebranding, we need a new website aimed towards the UK B2B marketplace.

The website needs to deliver a modern and creative website design whilst ensuring the design is tailored towards conversion optimisation.

This site must drive point of contact either from an online form, via a direct telephone call or Skype connection.

Our sales are all offline so the website will be a simple, elegant and stunning information portal.

Kolvex Digital offers Digital Marketing services to companies throughout the UK - our target audiences are companies that turnover a minimum of 3 million pounds a year and as such we need to deliver a professional image that installs confidence in our companies abilities.

We do not like websites that are reliant upon stock photography - we are happy for stock photography to be used in a small way however the site must not look like a template filled with stock photography.

What do we do

We supply digital marketing services to those companies who demand a strong return on investment - our company prides itself on delivering successful campaigns that help establish long-term profitable relationships.

A lot of the information presented on our old site is relevant today however the design sucks. So please use the information on our current website as a foundation for your design content.

I am looking for several page designs including

"Home Page" Desktop Version
"Service Page" Desktop Version
"Blog Page" Desktop Version

"Home Page" Mobile Version
"Service Page" Mobile Version
"Blog Page" Mobile Version

In the 1st instance please only submit a single design for the "Home Page" Desktop Version - those designers that we are impressed with will be asked to complete the other designs before a winner is selected.

I like modern clean fonts - the site needs to welcome the reader and encourage them to absorb the information - not to overload and make them leave.

The site must be designed to naturally fit our companies new logo.

NO TEMPLATES

Target Market(s)

B2b - 3 million turnover and above

Industry/Entity Type

Digital Marketing

Number of Pages Required

3 page

Requirements
Must have
• Blended well with the companies logo
• We need conversion optimisation to be a huge part of the design - we considered a conversation when a potential customer reaches out to use via - web form, telephone or skype
• The current content on the old website fits today's business but the design sucks.
• www.kolvexdigital-example.com
Nice to have
• We need 3 pages (in 2 variants Desktop and Mobile)
• Home Page
• Service Page
• Blog Page
• Please only deliver the "Home Page" desktop version - if we are happy with your design we will aks for the additional pages
Should not have
• No templates and not stock photo heavy design

```html
<!DOCTYPE html>
<html lang="en">
<head>
<meta charset="utf-8">
<title>Kolvex Digital – Search Marketing That Actually Delivers</title>
<link href="https://fonts.googleapis.com/css2?family=Montserrat:wght@300;400;500;600;700&family=Open+Sans:wght@400;600;700&display=swap" rel="stylesheet">
<style>
:root{
  --blue-deep:#0b469c;
  --blue:#1560c4;
  --blue-bright:#2a82e4;
  --blue-head:#1a58a8;
  --ink:#3a3f47;
  --muted:#8a9099;
  --line:#e3e7ec;
  --wash:#f2f5f9;
  --button:#6c6c6c;
  --footer:#7b7c7e;
  --white:#ffffff;
}
*{box-sizing:border-box;margin:0;padding:0}
html,body{width:1200px;height:3750px;overflow:hidden}
body{position:relative;background:var(--white);font-family:"Open Sans",Arial,sans-serif;color:var(--ink)}
.abs{position:absolute}
.heading{font-family:"Montserrat",Arial,sans-serif}

/* header */
.hero{left:0;top:0;width:1200px;height:500px;background:linear-gradient(135deg,var(--blue-deep) 0%,var(--blue) 60%,#1d70d6 100%);overflow:hidden}
.hero-wave{left:0;top:380px;width:1200px;height:130px}
.nav-logo{left:232px;top:12px;display:flex;align-items:center;gap:8px;color:var(--white);font-family:"Montserrat",sans-serif;font-weight:600;font-size:15px}
.nav-logo .mark{width:14px;height:14px;border:2px solid var(--white)}
.nav-links{left:455px;top:0;height:45px;display:flex;align-items:center;gap:26px;color:var(--white);font-size:11px;font-family:"Montserrat",sans-serif}
.nav-links .active{font-weight:600}
.nav-actions{left:862px;top:0;display:flex;gap:6px}
.nav-actions span{width:46px;height:45px;background:#0a3b85;display:flex;align-items:center;justify-content:center}
.hero-title{left:232px;top:158px;color:var(--white);font-size:29px;font-weight:400;line-height:36px}
.hero-sub{left:232px;top:240px;width:330px;color:#d6e5fa;font-size:11.5px;line-height:17px}
.btn-white{left:232px;top:298px;width:106px;height:28px;border-radius:14px;background:var(--white);color:var(--blue-head);font-size:10.5px;font-weight:600;display:flex;align-items:center;justify-content:center}
.hero-art{left:600px;top:95px;width:575px;height:235px;border-radius:30px;background:radial-gradient(ellipse at 55% 45%,rgba(255,255,255,.28) 0%,rgba(255,255,255,.08) 55%,rgba(255,255,255,0) 75%)}
.scroll-dot{width:28px;height:28px;border-radius:50%;background:var(--white);box-shadow:0 2px 6px rgba(0,0,0,.15);display:flex;align-items:center;justify-content:center}

/* ROI */
.roi-title{left:0;top:528px;width:1200px;text-align:center;color:var(--blue-head);font-size:20.5px;font-weight:500;line-height:29px}
.roi-text{left:270px;top:604px;width:660px;text-align:center;font-size:9.5px;line-height:16px;color:var(--muted)}
.roi-note{left:0;top:700px;width:1200px;text-align:center;font-size:10px;color:var(--muted)}
.badges{left:237px;top:737px;display:flex;gap:30px}
.badge{width:95px;height:58px;background:var(--white);border-radius:3px;box-shadow:0 2px 8px rgba(0,0,0,.1);display:flex;align-items:center;justify-content:center}
.badge i{display:block;width:56px;height:14px;border-radius:7px;background:#d7dce3}

/* services */
.services-bg{left:0;top:840px;width:1200px;height:800px}
.section-title{left:0;width:1200px;text-align:center;color:var(--blue-head);font-size:20px;font-weight:500}
.section-sub{left:0;width:1200px;text-align:center;color:var(--muted);font-size:10px}
.card{width:225px;height:222px;background:var(--white);box-shadow:0 2px 10px rgba(20,40,80,.08);text-align:center}
.card.featured{border-bottom:4px solid #3d4a5a;box-shadow:0 4px 14px rgba(20,40,80,.16)}
.card .icon{width:50px;height:50px;border-radius:50%;background:#eef3fa;margin:28px auto 0;display:flex;align-items:center;justify-content:center}
.card h3{font-family:"Montserrat",sans-serif;font-weight:500;font-size:13px;color:var(--blue-head);margin-top:16px}
.card p{font-size:9px;line-height:14px;color:var(--muted);margin:10px 22px 0}
.card .go{position:absolute;left:99px;bottom:-13px;width:27px;height:27px;border-radius:50%;background:#5f6368;display:flex;align-items:center;justify-content:center}
.card.featured .go{background:var(--blue)}
.btn-grey{width:106px;height:28px;border-radius:14px;background:var(--button);color:var(--white);font-size:10.5px;display:flex;align-items:center;justify-content:center;box-shadow:0 2px 6px rgba(0,0,0,.15)}

/* why */
.ring{left:455px;top:1792px;width:290px;height:290px;border-radius:50%;border:9px solid #eceff3;background:var(--white)}
.ring-logo{left:455px;top:1912px;width:290px;display:flex;align-items:center;justify-content:center;gap:10px;font-family:"Montserrat",sans-serif;font-weight:600;font-size:22px;color:#6b6f75}
.ring-logo .mark{width:18px;height:18px;background:#6b6f75}
.bubble{width:52px;height:52px;border-radius:50%;display:flex;align-items:center;justify-content:center;box-shadow:0 3px 8px rgba(0,0,0,.18)}
.bubble.dark{background:var(--blue-deep)}
.bubble.light{background:var(--blue-bright)}
.why-item{width:150px}
.why-item h4{font-family:"Montserrat",sans-serif;font-weight:500;font-size:11.5px;line-height:16px;color:var(--blue-head)}
.why-item p{font-size:9.5px;line-height:14px;color:var(--muted);margin-top:5px}
.why-item.left{text-align:left}

/* seo */
.seo-title{left:232px;top:2280px;font-size:20px;font-weight:500;color:var(--blue-head)}
.seo-sub{left:232px;top:2312px;font-size:13px;color:var(--muted);font-family:"Montserrat",sans-serif}
.seo-text{left:232px;top:2348px;width:365px;font-size:9.5px;line-height:15px;color:var(--muted)}
.seo-list-title{left:232px;top:2472px;font-size:11.5px;font-weight:600;color:var(--blue-head);font-family:"Montserrat",sans-serif}
.seo-list{left:232px;top:2500px;width:365px;list-style:none}
.seo-list li{display:flex;gap:8px;font-size:9.2px;line-height:14px;color:var(--muted);margin-bottom:11px}
.seo-list li svg{flex:none;margin-top:2px}
.seo-photo{left:612px;top:2262px;width:620px;height:428px;border-radius:220px 0 0 220px;background:linear-gradient(135deg,#c7ccd4 0%,#9aa3b0 45%,#6d7685 100%)}
.stats{left:695px;top:2337px;width:275px;height:343px;background:var(--blue-bright);box-shadow:0 6px 18px rgba(0,0,0,.2)}
.stats-head{height:80px;background:var(--blue-deep);color:var(--white);font-family:"Montserrat",sans-serif;font-size:11px;font-weight:600;line-height:17px;padding:22px 20px}
.stat{padding:0 20px;color:var(--white);margin-top:20px}
.stat b{display:block;font-family:"Montserrat",sans-serif;font-size:22px;font-weight:600;line-height:24px}
.stat span{font-size:9.5px}

/* testimonials */
.quote-band{left:0;top:2740px;width:1200px;height:520px}
.cs-icon{left:232px;top:2880px;width:46px;height:46px;border-radius:50%;border:2px solid var(--white);display:flex;align-items:center;justify-content:center}
.cs-title{left:232px;top:2944px;color:var(--white);font-size:20px;font-weight:500}
.cs-text{left:232px;top:2980px;width:190px;color:#dbe8fb;font-size:10px;line-height:15px}
.cs-btn{left:232px;top:3030px;width:96px;height:26px;border-radius:13px;background:var(--white);color:var(--blue-head);font-size:10px;display:flex;align-items:center;justify-content:center}
.quote{width:245px;height:185px;background:var(--white);padding:20px 28px;font-size:9px;line-height:14px;color:var(--muted)}
.quote .stars{margin-top:10px;display:flex;gap:3px}
.author{display:flex;align-items:center;gap:10px}
.author .avatar{width:40px;height:40px;border-radius:50%;background:#c9d3df;border:3px solid var(--white)}
.author b{display:block;color:var(--white);font-family:"Montserrat",sans-serif;font-size:10.5px;font-weight:500}
.author small{color:#9ec3f1;font-size:8.5px}

/* contact */
.talk-title{left:0;top:3250px;width:1200px;text-align:center;font-size:15px;font-weight:600;color:var(--blue-head)}
.talk-sub{left:450px;top:3282px;width:300px;text-align:center;font-size:11px;line-height:17px;color:var(--muted)}
.field{width:125px;height:28px;border:1px solid var(--line);border-radius:14px;background:var(--white);font-size:9.5px;color:#a3a8af;padding:0 14px;display:flex;align-items:center}

/* footer */
.footer-bg{left:0;top:3395px;width:1200px;height:355px}
.foot-logo{left:232px;top:3530px;display:flex;align-items:center;gap:8px;color:var(--white);font-family:"Montserrat",sans-serif;font-weight:600;font-size:14px}
.foot-logo .mark{width:12px;height:12px;border:2px solid var(--white)}
.foot-contact{left:232px;top:3573px;font-size:9.5px;line-height:17px;color:#eeeeee}
.foot-col{color:#eeeeee;font-size:9.5px;line-height:16px}
.foot-col h5{font-family:"Montserrat",sans-serif;font-size:11px;font-weight:600;color:var(--white);margin-bottom:12px}
.news-field{width:165px;height:26px;border-radius:13px;background:var(--white);font-size:9px;color:#a3a8af;padding:0 14px;display:flex;align-items:center;justify-content:space-between}
.socials{display:flex;gap:6px;margin-top:16px}
.socials span{width:20px;height:20px;border-radius:50%;background:var(--white)}
.copyright{left:0;top:3712px;width:1200px;text-align:center;font-size:9px;color:#e4e4e4}
</style>
</head>
<body>

<!-- Header -->
<section class="abs hero">
  <div class="abs hero-art" role="img" aria-label="Illustration of marketing icons linked in a network"></div>
  <div class="abs nav-logo"><span class="mark"></span>Kolvex Digital</div>
  <nav class="abs nav-links">
    <span class="active">Home</span><span>Services</span><span>White Lable Link Building</span><span>+44 (0) 1700 555 218</span>
  </nav>
  <div class="abs nav-actions">
    <span><svg width="16" height="12" viewBox="0 0 16 12"><rect x="1" y="1" width="14" height="10" fill="none" stroke="#fff" stroke-width="1.5"/><path d="M1 1l7 6 7-6" fill="none" stroke="#fff" stroke-width="1.5"/></svg></span>
    <span><svg width="14" height="14" viewBox="0 0 14 14"><circle cx="7" cy="7" r="6" fill="none" stroke="#fff" stroke-width="1.5"/></svg></span>
  </div>
  <h1 class="abs heading hero-title">Search Marketing<br>That Actually Delivers</h1>
  <p class="abs hero-sub">Search marketing is our forte. Our clients results highlight just how we do it.</p>
  <div class="abs btn-white">Get Started</div>
  <svg class="abs hero-wave" viewBox="0 0 1200 130" preserveAspectRatio="none">
    <path d="M0 40 C300 120 700 10 1200 60 L1200 130 L0 130Z" fill="#5d9be6" opacity=".5"/>
    <path d="M0 60 C320 125 720 30 1200 80 L1200 130 L0 130Z" fill="#dbe8f8"/>
    <path d="M0 75 C340 130 760 50 1200 95 L1200 130 L0 130Z" fill="#ffffff"/>
  </svg>
</section>
<div class="abs scroll-dot" style="left:586px;top:446px"><svg width="10" height="10" viewBox="0 0 10 10"><path d="M5 1v7M2 5l3 3 3-3" fill="none" stroke="#1560c4" stroke-width="1.6"/></svg></div>

<!-- ROI -->
<h2 class="abs heading roi-title">Do you want to see an enviable ROI on search marketing?<br>It’s possible – you’ve found us.</h2>
<p class="abs roi-text">We know and understand the world of business. We know that ROI is the single most important metric in the marketing world. We’ve worked with some of the world’s largest industries – such as finance, insurance, payday loans and health, where achieving above 100% ROI is often impossible. For us, it’s just a challenge that can be overcome. Whether we’re working with you to drive your Pay-Per-Click Marketing, Organic Search Marketing (SEO), Email Marketing or Lead Filtering &amp; Delivery – we always have your ROI in mind. That’s why we’re known as the ROI driven digital agency.</p>
<p class="abs roi-note">Handle your SEO in-house? Consider using our industry-leading link outreach service to bolster your efforts.</p>
<div class="abs badges">
  <div class="badge"><i></i></div><div class="badge"><i></i></div><div class="badge"><i></i></div>
  <div class="badge"><i></i></div><div class="badge"><i></i></div><div class="badge"><i></i></div>
</div>

<!-- Services -->
<svg class="abs services-bg" viewBox="0 0 1200 800" preserveAspectRatio="none">
  <path d="M0 40 C350 0 800 80 1200 20 L1200 740 C800 800 400 700 0 770Z" fill="#f2f5f9"/>
</svg>
<div class="abs scroll-dot" style="left:586px;top:874px"><svg width="10" height="10" viewBox="0 0 10 10"><path d="M5 1v7M2 5l3 3 3-3" fill="none" stroke="#1560c4" stroke-width="1.6"/></svg></div>
<h2 class="abs heading section-title" style="top:967px">Our Services</h2>
<p class="abs section-sub" style="top:1004px">Grow your business and save time with seamless experience</p>

<div class="abs card featured" style="left:237px;top:1055px">
  <div class="icon"><svg width="22" height="22" viewBox="0 0 22 22"><circle cx="9" cy="9" r="6" fill="none" stroke="#1560c4" stroke-width="2"/><path d="M13.5 13.5L20 20" stroke="#1560c4" stroke-width="2.4"/></svg></div>
  <h3>Organic Search</h3>
  <p>Attract traffic that converts and interacts with your brand through Organic. We implement both short-term and long-term campaigns to bolster your success.</p>
  <span class="go"><svg width="10" height="10" viewBox="0 0 10 10"><path d="M1 5h7M5 2l3 3-3 3" fill="none" stroke="#fff" stroke-width="1.6"/></svg></span>
</div>
<div class="abs card" style="left:487px;top:1055px">
  <div class="icon"><svg width="22" height="22" viewBox="0 0 22 22"><circle cx="9" cy="9" r="6" fill="none" stroke="#1560c4" stroke-width="2"/><path d="M13.5 13.5L20 20" stroke="#1560c4" stroke-width="2.4"/><path d="M9 6v6M7 8h4" stroke="#1560c4" stroke-width="1.4"/></svg></div>
  <h3>Paid Search</h3>
  <p>Drive highly converting traffic to your website. Our PPC campaigns are ROI driven from the start – helping you to scale your business quickly.</p>
  <span class="go"><svg width="10" height="10" viewBox="0 0 10 10"><path d="M1 5h7M5 2l3 3-3 3" fill="none" stroke="#fff" stroke-width="1.6"/></svg></span>
</div>
<div class="abs card" style="left:740px;top:1055px">
  <div class="icon"><svg width="20" height="22" viewBox="0 0 20 22"><path d="M3 1h10l5 5v15H3Z" fill="none" stroke="#1560c4" stroke-width="1.8"/><path d="M6 11h8M6 15h8" stroke="#1560c4" stroke-width="1.5"/></svg></div>
  <h3>Link Outreach</h3>
  <p>The core foundation of any search campaign. Our team of link outreachers are the best in the industry. We secure link placements that drive rankings.</p>
  <span class="go"><svg width="10" height="10" viewBox="0 0 10 10"><path d="M1 5h7M5 2l3 3-3 3" fill="none" stroke="#fff" stroke-width="1.6"/></svg></span>
</div>
<div class="abs card" style="left:237px;top:1305px">
  <div class="icon"><svg width="22" height="22" viewBox="0 0 22 22"><circle cx="5" cy="11" r="3" fill="none" stroke="#1560c4" stroke-width="1.8"/><circle cx="17" cy="4" r="3" fill="none" stroke="#1560c4" stroke-width="1.8"/><circle cx="17" cy="18" r="3" fill="none" stroke="#1560c4" stroke-width="1.8"/><path d="M7.6 9.6l6.8-4M7.6 12.4l6.8 4" stroke="#1560c4" stroke-width="1.6"/></svg></div>
  <h3>Social Media</h3>
  <p>Attract traffic that converts and interacts with your brand through Organic. We implement both short-term and long-term campaigns to bolster your success.</p>
  <span class="go"><svg width="10" height="10" viewBox="0 0 10 10"><path d="M1 5h7M5 2l3 3-3 3" fill="none" stroke="#fff" stroke-width="1.6"/></svg></span>
</div>
<div class="abs card" style="left:487px;top:1305px">
  <div class="icon"><svg width="24" height="20" viewBox="0 0 24 20"><rect x="1" y="1" width="22" height="15" fill="none" stroke="#1560c4" stroke-width="1.8"/><path d="M5 12l4-4 3 3 5-5" fill="none" stroke="#1560c4" stroke-width="1.6"/><path d="M8 19h8" stroke="#1560c4" stroke-width="1.8"/></svg></div>
  <h3>UX &amp; CRO</h3>
  <p>Drive highly converting traffic to your website. Our PPC campaigns are ROI driven from the start – helping you to scale your business quickly.</p>
  <span class="go"><svg width="10" height="10" viewBox="0 0 10 10"><path d="M1 5h7M5 2l3 3-3 3" fill="none" stroke="#fff" stroke-width="1.6"/></svg></span>
</div>
<div class="abs card" style="left:740px;top:1305px">
  <div class="icon"><svg width="20" height="22" viewBox="0 0 20 22"><path d="M3 1h10l5 5v15H3Z" fill="none" stroke="#1560c4" stroke-width="1.8"/><path d="M6 9l4 3 4-3" fill="none" stroke="#1560c4" stroke-width="1.5"/></svg></div>
  <h3>Email Marketing</h3>
  <p>The core foundation of any search campaign. Our team of link outreachers are the best in the industry. We secure link placements that drive rankings.</p>
  <span class="go"><svg width="10" height="10" viewBox="0 0 10 10"><path d="M1 5h7M5 2l3 3-3 3" fill="none" stroke="#fff" stroke-width="1.6"/></svg></span>
</div>
<div class="abs btn-grey" style="left:547px;top:1618px">Get Started</div>

<!-- Why choose -->
<h2 class="abs heading section-title" style="top:1692px">Why Choose Kolvex Digital</h2>
<p class="abs section-sub" style="top:1728px">Grow your business and save time with seamless experience</p>
<div class="abs ring"></div>
<div class="abs ring-logo"><span class="mark"></span>Kolvex Digital</div>

<div class="abs bubble dark" style="left:474px;top:1811px"><svg width="22" height="22" viewBox="0 0 22 22"><circle cx="11" cy="11" r="8" fill="none" stroke="#fff" stroke-width="1.8"/><circle cx="11" cy="11" r="3.5" fill="none" stroke="#fff" stroke-width="1.8"/></svg></div>
<div class="abs bubble light" style="left:678px;top:1811px"><svg width="22" height="22" viewBox="0 0 22 22"><path d="M4 18l4-8 8-7-1 9-7 4Z" fill="#fff"/></svg></div>
<div class="abs bubble light" style="left:474px;top:2011px"><svg width="22" height="20" viewBox="0 0 22 20"><path d="M2 7l4-5h10l4 5-9 11Z" fill="none" stroke="#fff" stroke-width="1.8"/><path d="M2 7h18" stroke="#fff" stroke-width="1.5"/></svg></div>
<div class="abs bubble dark" style="left:678px;top:2011px"><svg width="20" height="20" viewBox="0 0 20 20"><rect x="2" y="9" width="4" height="9" fill="#fff"/><path d="M8 9l4-7c2 0 2 2 1.5 4H18v4l-2 8H8Z" fill="#fff"/></svg></div>

<div class="abs why-item" style="left:290px;top:1810px"><h4>Helping you to increase<br>your site traffic</h4><p>Lorem ipsum dolor sit amet, consectetur adipiscing elit sed tristique.</p></div>
<div class="abs why-item left" style="left:768px;top:1810px"><h4>Helping you to increase<br>your site traffic</h4><p>Lorem ipsum dolor sit amet, consectetur adipiscing elit sed tristique.</p></div>
<div class="abs why-item" style="left:290px;top:2004px"><h4>Helping you to increase<br>your site traffic</h4><p>Lorem ipsum dolor sit amet, consectetur adipiscing elit sed tristique.</p></div>
<div class="abs why-item left" style="left:768px;top:2004px"><h4>Helping you to increase<br>your site traffic</h4><p>Lorem ipsum dolor sit amet, consectetur adipiscing elit sed tristique.</p></div>
<div class="abs btn-grey" style="left:547px;top:2156px">Get Started</div>

<!-- SEO -->
<div class="abs seo-photo" role="img" aria-label="Photo of a laptop showing analytics charts on a desk"></div>
<h2 class="abs heading seo-title">Handle SEO Yourself? Perfect.</h2>
<p class="abs seo-sub">Hassle-Free Link Placements That Drive Rankings</p>
<p class="abs seo-text">Our link placements are used by some of the world’s largest companies in the most difficult industries – such as payday loans, insurance, finance, health and legal. We use our link placement service in conjunction with our Organic Search (SEO) offerings, although some of our clients handle their SEO in-house and prefer to use our link placements to bolster their rankings.</p>
<p class="abs seo-list-title">Here’s how our unique, link acquisition process works:</p>
<ul class="abs seo-list">
  <li><svg width="11" height="11" viewBox="0 0 11 11"><circle cx="5.5" cy="5.5" r="5.5" fill="#1560c4"/><path d="M3 5.7l1.8 1.8L8 4" fill="none" stroke="#fff" stroke-width="1.3"/></svg>We take your clients URLs and their business sector (or your own sites), and we utilise our connections to try and secure a link placement.</li>
  <li><svg width="11" height="11" viewBox="0 0 11 11"><circle cx="5.5" cy="5.5" r="5.5" fill="#1560c4"/><path d="M3 5.7l1.8 1.8L8 4" fill="none" stroke="#fff" stroke-width="1.3"/></svg>All of the sites we outreach too are 100% genuine – we do not own nor control any of the sites.</li>
  <li><svg width="11" height="11" viewBox="0 0 11 11"><circle cx="5.5" cy="5.5" r="5.5" fill="#1560c4"/><path d="M3 5.7l1.8 1.8L8 4" fill="none" stroke="#fff" stroke-width="1.3"/></svg>If a webmaster chooses to link to you, it is of their own accord. They have decided to link to you. Thus, you have earned a genuine link.</li>
  <li><svg width="11" height="11" viewBox="0 0 11 11"><circle cx="5.5" cy="5.5" r="5.5" fill="#1560c4"/><path d="M3 5.7l1.8 1.8L8 4" fill="none" stroke="#fff" stroke-width="1.3"/></svg>We will identify the most relevant page (post or thier site), and work with the webmaster to weave your links into their existing content. We will craft an additional sentence or two to make sure the anchor text fits in with the content.</li>
</ul>
<div class="abs stats">
  <div class="stats-head">We grow as our clients grow.<br>That’s what we love.</div>
  <div class="stat"><b>117</b><span>Satisfied Clients</span></div>
  <div class="stat"><b>215</b><span>Campaigns Finished</span></div>
  <div class="stat"><b>1,798</b><span>Cups of Coffee</span></div>
</div>

<!-- Testimonials -->
<svg class="abs quote-band" viewBox="0 0 1200 520" preserveAspectRatio="none">
  <defs><linearGradient id="bandGrad" x1="0" y1="0" x2="1" y2="0"><stop offset="0" stop-color="#0b469c"/><stop offset="1" stop-color="#2a82e4"/></linearGradient></defs>
  <path d="M0 10 C350 70 800 0 1200 40 L1200 470 C850 520 350 430 0 500Z" fill="#cfe0f6"/>
  <path d="M0 35 C350 95 800 25 1200 60 L1200 450 C850 500 350 410 0 480Z" fill="url(#bandGrad)"/>
</svg>
<div class="abs cs-icon"><svg width="22" height="18" viewBox="0 0 22 18"><path d="M2 10c0-5 3-8 7-9v3c-2 1-3 2-3 4h3v8H2Zm11 0c0-5 3-8 7-9v3c-2 1-3 2-3 4h3v8h-7Z" fill="none" stroke="#fff" stroke-width="1.5"/></svg></div>
<h2 class="abs heading cs-title">Customer Speaks</h2>
<p class="abs cs-text">Lorem ipsum dolor sit amet, consectetur adip elit hendrerit</p>
<div class="abs cs-btn">Read All</div>

<div class="abs quote" style="left:480px;top:2887px">Mauris rutrum justo justo, quis vestibulum ligula facilisis id. In pellentesque imperdiet nisl ut bibendum. Nunc malesuada felis vel tincidunt molestie. In tristique ante id dictum pulvinar.<div class="stars"><svg width="60" height="10" viewBox="0 0 60 10"><g fill="none" stroke="#b5bcc6" stroke-width=".8"><path d="M5 1l1.2 2.6 2.8.3-2.1 1.9.6 2.8L5 7.2 2.5 8.6l.6-2.8L1 3.9l2.8-.3Z"/><path transform="translate(12 0)" d="M5 1l1.2 2.6 2.8.3-2.1 1.9.6 2.8L5 7.2 2.5 8.6l.6-2.8L1 3.9l2.8-.3Z"/><path transform="translate(24 0)" d="M5 1l1.2 2.6 2.8.3-2.1 1.9.6 2.8L5 7.2 2.5 8.6l.6-2.8L1 3.9l2.8-.3Z"/><path transform="translate(36 0)" d="M5 1l1.2 2.6 2.8.3-2.1 1.9.6 2.8L5 7.2 2.5 8.6l.6-2.8L1 3.9l2.8-.3Z"/><path transform="translate(48 0)" d="M5 1l1.2 2.6 2.8.3-2.1 1.9.6 2.8L5 7.2 2.5 8.6l.6-2.8L1 3.9l2.8-.3Z"/></g></svg></div></div>
<div class="abs quote" style="left:755px;top:2887px">Mauris rutrum justo justo, quis vestibulum ligula facilisis id. In pellentesque imperdiet nisl ut bibendum. Nunc malesuada felis vel tincidunt molestie. In tristique ante id dictum pulvinar.<div class="stars"><svg width="60" height="10" viewBox="0 0 60 10"><g fill="none" stroke="#b5bcc6" stroke-width=".8"><path d="M5 1l1.2 2.6 2.8.3-2.1 1.9.6 2.8L5 7.2 2.5 8.6l.6-2.8L1 3.9l2.8-.3Z"/><path transform="translate(12 0)" d="M5 1l1.2 2.6 2.8.3-2.1 1.9.6 2.8L5 7.2 2.5 8.6l.6-2.8L1 3.9l2.8-.3Z"/><path transform="translate(24 0)" d="M5 1l1.2 2.6 2.8.3-2.1 1.9.6 2.8L5 7.2 2.5 8.6l.6-2.8L1 3.9l2.8-.3Z"/><path transform="translate(36 0)" d="M5 1l1.2 2.6 2.8.3-2.1 1.9.6 2.8L5 7.2 2.5 8.6l.6-2.8L1 3.9l2.8-.3Z"/><path transform="translate(48 0)" d="M5 1l1.2 2.6 2.8.3-2.1 1.9.6 2.8L5 7.2 2.5 8.6l.6-2.8L1 3.9l2.8-.3Z"/></g></svg></div></div>
<div class="abs quote" style="left:1030px;top:2887px">Mauris rutrum justo justo, quis vestibulum ligula facilisis id. In pellentesque imperdiet nisl ut bibendum. Nunc malesuada felis vel tincidunt molestie. In tristique ante id dictum pulvinar.</div>

<div class="abs author" style="left:480px;top:3095px"><span class="avatar" role="img" aria-label="Client portrait"></span><div><b>Daniel Hartley</b><small>Chief Digital Officer</small></div></div>
<div class="abs author" style="left:755px;top:3095px"><span class="avatar" role="img" aria-label="Client portrait"></span><div><b>Daniel Hartley</b><small>Chief Digital Officer</small></div></div>
<div class="abs author" style="left:1030px;top:3095px"><span class="avatar" role="img" aria-label="Client portrait"></span><div><b>Daniel Hartley</b><small>Chief Digital Officer</small></div></div>

<!-- Contact -->
<h2 class="abs heading talk-title">Want To Improve Your ROI? Let’s Talk.</h2>
<p class="abs talk-sub">We’ll never turn down an opportunity to discover how we can help grow your business.</p>
<div class="abs field" style="left:330px;top:3336px">Name</div>
<div class="abs field" style="left:475px;top:3336px">Email</div>
<div class="abs field" style="left:620px;top:3336px">Phone</div>
<div class="abs btn-grey" style="left:760px;top:3336px;width:122px">Get Started</div>

<!-- Footer -->
<svg class="abs footer-bg" viewBox="0 0 1200 355" preserveAspectRatio="none">
  <path d="M0 40 C300 70 700 -10 1200 25 L1200 355 L0 355Z" fill="#e6e9ed"/>
  <path d="M0 55 C320 85 720 10 1200 45 L1200 355 L0 355Z" fill="#7b7c7e"/>
</svg>
<div class="abs scroll-dot" style="left:586px;top:3432px"><svg width="10" height="10" viewBox="0 0 10 10"><path d="M5 9V2M2 5l3-3 3 3" fill="none" stroke="#1560c4" stroke-width="1.6"/></svg></div>
<div class="abs foot-logo"><span class="mark"></span>Kolvex Digital</div>
<div class="abs foot-contact">01700 555 218<br>hello@kolvexdigital-example.com</div>
<div class="abs foot-col" style="left:418px;top:3525px"><h5>Our Key Services</h5>Link Outreach<br>Organic Search (SEO)<br>Paid Search (PPC)<br>Social Media Marketing</div>
<div class="abs foot-col" style="left:595px;top:3525px"><h5>Locations We Cover (SEO)</h5>Birmingham<br>Essex<br>London<br>Manchester<br>See All Locations We Cover (SEO)</div>
<div class="abs foot-col" style="left:802px;top:3525px"><h5>Subscribe Newsletter</h5>
  <div class="news-field">Email ID<svg width="10" height="10" viewBox="0 0 10 10"><path d="M1 5h7M5 2l3 3-3 3" fill="none" stroke="#7b7c7e" stroke-width="1.5"/></svg></div>
  <div class="socials"><span></span><span></span><span></span><span></span></div>
</div>
<div class="abs" style="left:232px;top:3700px;width:736px;height:1px;background:#8f9092"></div>
<p class="abs copyright">2018 © Copyright Kolvex Digital Ltd. All Rights Reserved.</p>

</body>
</html>
```